Business Card for Bright Furrow Lawn & Landscape

Double Sided Card Design - I think one side of the card should be cleaner, with logo, contact info, and "Complete Residential & Commercial Landscape Services", and on the other side it should list the services we offer:

- Lawn Care & Mowing
- Hedge & Shrub Trimming
- Leaf Removal & Clean Up
- Aeration & Sod
- Mulch & Rock Installations
- Landscape Installations & Renovations
- Commercial Snow Removal

Please make it clean and very professional... don't want it too be too busy, but want to tell them what we do.

Target Market(s)

Residential and Commercial

Industry/Entity Type

Landscape

Contact Information for Business Card

Fully Insured
Dale Ostrov
410-372-6184
Dostrov07@quillpost.net

Requirements
Must have
• Double Sided, Cleaner on one side, more information and text on the other side.

```html
<!DOCTYPE html>
<html lang="en">
<head>
<meta charset="utf-8">
<title>Bright Furrow Lawn &amp; Landscape – Business Card</title>
<link rel="stylesheet" href="https://fonts.googleapis.com/css2?family=Cinzel:wght@600&family=Open+Sans:wght@400&display=swap">
<style>
  :root {
    --page-bg: #e9e6e1;
    --card-bg: #1f1f1f;
    --brand-green: #80b440;
    --text-light: #f2f2f2;
    --swoosh-white: #ffffff;
    --grass-shade: #2a2d27;
  }
  * { margin: 0; padding: 0; box-sizing: border-box; }
  html, body { width: 1200px; height: 1000px; overflow: hidden; }
  body {
    background: var(--page-bg);
    position: relative;
    font-family: "Open Sans", Arial, sans-serif;
    color: var(--text-light);
  }
  .card {
    position: absolute;
    left: 266px;
    width: 666px;
    height: 397px;
    background: var(--card-bg);
    overflow: hidden;
    box-shadow: 0 4px 14px rgba(0,0,0,0.35);
  }
  .card--services { top: 74px; }
  .card--contact { top: 533px; }

  /* Services side */
  .service-list {
    position: absolute;
    left: 33px;
    top: 68px;
    list-style: none;
  }
  .service-list li {
    display: flex;
    align-items: center;
    height: 39px;
    font-size: 16.5px;
  }
  .service-list li::before {
    content: "";
    width: 15px;
    height: 15px;
    border-radius: 50%;
    border: 2px solid var(--brand-green);
    margin-right: 9px;
    flex: none;
  }
  .brand {
    position: absolute;
    text-align: center;
    font-family: "Cinzel", "Times New Roman", serif;
    font-weight: 600;
    color: var(--brand-green);
    line-height: 1.05;
  }
  .brand-dot {
    display: block;
    margin: 0 auto 14px;
    border-radius: 50%;
    border: 7px solid var(--brand-green);
  }
  .brand-name { display: block; }
  .brand-tag { display: block; letter-spacing: 2.5px; }

  .card--services .brand { left: 380px; width: 270px; top: 118px; }
  .card--services .brand-dot { width: 84px; height: 84px; }
  .card--services .brand-name { font-size: 27px; }
  .card--services .brand-tag { font-size: 15.5px; margin-top: 4px; }

  /* Contact side */
  .card--contact .brand { left: 20px; width: 300px; top: 45px; }
  .card--contact .brand-dot { width: 104px; height: 104px; margin-bottom: 20px; }
  .card--contact .brand-name { font-size: 31px; }
  .card--contact .brand-tag { font-size: 17px; margin-top: 4px; }

  .grass-backdrop {
    position: absolute;
    left: 390px;
    top: 110px;
    width: 250px;
    height: 225px;
    background: radial-gradient(ellipse at 50% 70%, var(--grass-shade) 0%, rgba(42,45,39,0.4) 55%, rgba(31,31,31,0) 75%);
  }
  .holder-name {
    position: absolute;
    left: 420px;
    top: 172px;
    width: 244px;
    text-align: center;
    font-family: "Cinzel", "Times New Roman", serif;
    font-weight: 600;
    font-size: 25px;
    color: var(--brand-green);
    letter-spacing: 0.5px;
  }
  .contact-details {
    position: absolute;
    left: 39px;
    top: 245px;
    font-size: 16.5px;
    line-height: 25px;
  }
  .contact-details .insured { margin-bottom: 3px; }
  .contact-line { display: flex; align-items: center; }
  .contact-line svg { width: 14px; height: 14px; margin-right: 8px; flex: none; }
  .swoosh {
    position: absolute;
    left: 0;
    bottom: 0;
    width: 666px;
    height: 80px;
  }
</style>
</head>
<body>

<section class="card card--services" aria-label="Services side">
  <ul class="service-list">
    <li>Lawn Care &amp; Mowing</li>
    <li>Hedge &amp; Shrub Trimming</li>
    <li>Leaf Removal &amp; Clean Up</li>
    <li>Aeration &amp; Sod</li>
    <li>Mulch &amp; Rock Installations</li>
    <li>Landscape Installations &amp; Renovations</li>
    <li>Commercial Snow Removal</li>
  </ul>
  <div class="brand">
    <span class="brand-dot"></span>
    <span class="brand-name">Bright Furrow</span>
    <span class="brand-tag">LAWN &amp; LANDSCAPE</span>
  </div>
</section>

<section class="card card--contact" aria-label="Contact side">
  <div class="grass-backdrop" role="img" aria-label="Faint grass blade decoration"></div>
  <div class="brand">
    <span class="brand-dot"></span>
    <span class="brand-name">Bright Furrow</span>
    <span class="brand-tag">LAWN &amp; LANDSCAPE</span>
  </div>
  <div class="holder-name">DALE OSTROV</div>
  <div class="contact-details">
    <div class="insured">Fully Insured</div>
    <div class="contact-line">
      <svg viewBox="0 0 16 16" aria-hidden="true"><path fill="#80b440" d="M2 6c0-2 2-3 6-3s6 1 6 3v1h-3V5.5H5V7H2zM4 8h8l2 6H2z"/></svg>
      <span>410-372-6184</span>
    </div>
    <div class="contact-line">
      <svg viewBox="0 0 16 16" aria-hidden="true"><rect x="1" y="3" width="14" height="10" fill="#80b440"/><path d="M1 3l7 6 7-6" fill="none" stroke="#1f1f1f" stroke-width="1.4"/></svg>
      <span>Dostrov07@quillpost.net</span>
    </div>
  </div>
  <svg class="swoosh" viewBox="0 0 666 80" preserveAspectRatio="none" aria-hidden="true">
    <path d="M0 70 C180 20 420 2 600 0 L590 6 C400 10 190 40 0 80 Z" fill="var(--swoosh-white)"/>
    <path d="M0 80 C190 40 400 10 590 6 L666 8 L666 80 Z" fill="var(--brand-green)"/>
  </svg>
</section>

</body>
</html>
```